Need simple and modern looking business card with all my information on one side and logo on the other side
Info :
Company name - VELTRIN CONSTRUCTION LLC
Company addres- 418 maple 307th. Dunford hill ny 10583
Email- veltrinllc@pormail.Com
Company phone number 555-318-4096
Cell number- 555-762-0384
Web site - veltrinllc.Com
My name Gerald haverstrom

Target Market(s)

Construction , home improvement, remodeling

Industry/Entity Type

Construction

Contact Information for Business Card

It has to be moder but at the same time simple

Font styles to use
Sans Serif

Colors
0255a3
ffffff
000000
f78f20
b1b1b1
9d9d9d
1b1b1b
33a6d7
ec1f27

Requirements
Must have
• My logo on one side maybe with a some kind of background on the other side all my information
Nice to have
• Some kind of background pictures provided by you .PLEASE HAVE ACCOUNT WITH PIXVALEMOR WILL NOT PAY ANY EXTRA FEES .
Should not have
• Any kind of hamer, nails,screws, helmets itp. Please do not copy the other designs come up with something new.

```html
<!DOCTYPE html>
<html lang="en">
<head>
<meta charset="utf-8">
<title>Veltrin Construction LLC – Business Card</title>
<link href="https://fonts.googleapis.com/css2?family=Saira:wght@400;500&display=swap" rel="stylesheet">
<style>
  :root {
    --backdrop: #2b2724;
    --card: #1b1d20;
    --card-edge: #15171a;
    --ink: #ffffff;
    --logo-grey: #9d9d9d;
    --accent-orange: #f78f20;
    --tint-blue: rgba(2, 85, 163, .22);
    --tint-red: rgba(236, 31, 39, .16);
    --tint-orange: rgba(247, 143, 32, .14);
  }
  * { box-sizing: border-box; margin: 0; padding: 0; }
  html, body {
    width: 1200px; height: 769px; overflow: hidden;
    background: var(--backdrop);
    font-family: "Saira", Arial, sans-serif;
  }
  .stage {
    position: relative; width: 1200px; height: 769px;
    display: flex; align-items: center; justify-content: center; gap: 60px;
  }
  .card {
    position: relative; width: 500px; height: 286px; overflow: hidden;
    background: var(--card);
    border: 1px solid var(--card-edge);
    box-shadow: 0 18px 40px rgba(0,0,0,.45);
  }
  /* Front: company name */
  .card--front { display: flex; align-items: center; justify-content: center; }
  .brand { display: flex; align-items: center; gap: 14px; }
  .brand__mark { width: 14px; height: 14px; background: var(--logo-grey); }
  .brand__name {
    color: var(--logo-grey); font-weight: 500; font-size: 24px;
    letter-spacing: 2px;
  }
  /* Back: soft colour wash behind the details */
  .back-wash {
    position: absolute; right: 0; bottom: 0; width: 300px; height: 230px;
    background:
      radial-gradient(ellipse 120px 110px at 30% 65%, var(--tint-blue), transparent 70%),
      radial-gradient(ellipse 100px 90px at 72% 30%, var(--tint-red), transparent 70%),
      radial-gradient(ellipse 90px 80px at 80% 85%, var(--tint-orange), transparent 70%);
  }
  .contact { position: absolute; left: 38px; top: 60px; color: var(--ink); }
  .contact__header { border-left: 2px solid var(--accent-orange); padding-left: 12px; margin-bottom: 8px; }
  .contact__name { font-size: 22px; font-weight: 500; line-height: 1.2; }
  .contact__role { font-size: 15px; line-height: 1.2; }
  .contact__lines { font-size: 13px; line-height: 1.45; }
  .contact__row { display: flex; align-items: center; gap: 6px; }
  .contact__row svg { width: 11px; height: 11px; fill: var(--ink); flex: none; }
  .contact__gap { width: 8px; }
  .website {
    position: absolute; right: 28px; bottom: 24px;
    color: var(--ink); font-size: 14px;
  }
</style>
</head>
<body>
<main class="stage">
  <section class="card card--front" aria-label="Card front">
    <div class="brand">
      <span class="brand__mark"></span>
      <span class="brand__name">VELTRIN CONSTRUCTION LLC</span>
    </div>
  </section>

  <section class="card card--back" aria-label="Card back">
    <div class="back-wash" aria-hidden="true"></div>
    <div class="contact">
      <div class="contact__header">
        <p class="contact__name">Gerald haverstrom</p>
        <p class="contact__role">owner</p>
      </div>
      <div class="contact__lines">
        <p>418 maple 307th.</p>
        <p>Dunford hill ny 10583</p>
        <p class="contact__row">
          <svg viewBox="0 0 16 16" aria-hidden="true"><path d="M3 1h3l1.5 4-2 1.3a9 9 0 0 0 4.2 4.2L11 8.5l4 1.5v3a2 2 0 0 1-2 2A13 13 0 0 1 1 3a2 2 0 0 1 2-2z"/></svg>
          555-318-4096
          <span class="contact__gap"></span>
          <svg viewBox="0 0 16 16" aria-hidden="true"><path d="M4.5 0h7A1.5 1.5 0 0 1 13 1.5v13a1.5 1.5 0 0 1-1.5 1.5h-7A1.5 1.5 0 0 1 3 14.5v-13A1.5 1.5 0 0 1 4.5 0zM5 2v10h6V2z"/></svg>
          555-762-0384
        </p>
        <p class="contact__row">
          <svg viewBox="0 0 16 16" aria-hidden="true"><path d="M1 3h14v10H1zM2 4.2v.3l6 4 6-4v-.3z"/></svg>
          veltrinllc@pormail.Com
        </p>
      </div>
    </div>
    <p class="website">www.veltrinllc.com</p>
  </section>
</main>
</body>
</html>
```